Corporate Identity Pack - LetterHead, Business Card, Envelope

We are looking for a clean, professional, and visually connected corporate identity set for our company "VELTA HOME" (Cleaning, Gardening, and Pest Control services).

The pack must include:

Business Card (front and back)
Envelope with recipient window on the right side (22x11)
A4 Letterhead

We provide:
Our final logo (PNG)
Three design references (Inspiration1, Inspiration2, Inspiration3) to spark ideas — but you are absolutely free to propose your own creative solutions based on these concepts.

What we want:
A clean, modern, and trustworthy style
A subtle but creative watermark or graphic detail on the letterhead (not too invasive)

The same visual "family feeling" across business card, envelope, and letterhead: designs must be different but clearly connected

Strong readability for all text and contact details

Use our brand colors (Navy Blue, Green, Orange/Red) in a smart, non-overloaded way

No strict limitations: we are open to creative proposals as long as they are coherent, elegant, and suitable for professional use

Technical specifications:
100% full A4 page layout (no accidental borders)

Deliver ready-to-print PDFs and vector files (AI, EPS)

Respect 5 mm safety margins

Standard sizes for A4, business card, envelope C6 with window at the right

Tone:
Modern – Clean – Elegant – Creative – Trustworthy

Target Market(s)

Professional businesses, property managers, condominium administrators, companies, clinics, and offices requiring cleaning, gardening, and pest control services. The design must convey trust, reliability, professionalism, and attention to detail.

Industry/Entity Type

Cleaning Services, Gardening Services, Pest Control Services

Colors
0054AA
0677BA
7BADD7
CADEEF
E8F1F8
59FF00
82FF00
B8FF75
E3FFCB
F4FFEA
EB3D1F
EC4F4E
F09395
F8D3D4
FCEDEE

Requirements
Must have
• Cohesive design across business card, letterhead, and envelope Clean, modern, professional look Use of brand colors: Navy Blue (main), Green, Orange/Red accents Letterhead must include a subtle watermark without interfering with text Envelope must be with a transparent window for recipient address visibility High readability of all text and contact details Proper alignment, no unnecessary margins (full A4 layout)
Nice to have
• Creative but discreet use of the checkmark from the logo as part of the background or watermark Slight variation or accent of color tones while respecting brand identity A clean visual accent that gives a sense of movement or dynamic professionalism (without being distracting) Icons for email, phone, and website on the business card (if stylistically appropriate)
Should not have
• Overuse of colors or rainbow effects Heavy backgrounds or complex textures that interfere with readability Fonts that are too playful, comic-style, or non-professional Overcrowded layouts — the design must feel clean and spacious Watermarks that are too strong or central (they must be subtle and marginal)

```html
<!DOCTYPE html>
<html lang="en">
<head>
<meta charset="utf-8">
<title>VELTA HOME – Stationery Set</title>
<link href="https://fonts.googleapis.com/css2?family=Poppins:wght@300;400;500;600;700&display=swap" rel="stylesheet">
<style>
  :root {
    --navy: #0b0a6b;
    --green: #6ccf2f;
    --orange: #ff6a13;
    --paper: #ffffff;
    --stage: #e4e6e9;
    --ink: #2a2c33;
    --muted: #8a8f99;
    --window: #d4d6da;
  }
  * { margin: 0; padding: 0; box-sizing: border-box; }
  html, body { width: 1200px; height: 888px; overflow: hidden; }
  body { background: var(--stage); font-family: "Poppins", sans-serif; color: var(--ink); position: relative; }

  .sheet { position: absolute; background: var(--paper); overflow: hidden; }
  .wordmark { position: absolute; display: flex; align-items: center; color: var(--navy); font-weight: 600; white-space: nowrap; letter-spacing: 0.02em; }
  .wordmark .mark-square { background: var(--navy); margin-right: 0.4em; flex: none; }
  .contact-row { display: flex; align-items: center; gap: 4px; white-space: nowrap; }
  .icon { flex: none; display: block; }

  /* Business card front */
  .card-front { left: 64px; top: 62px; width: 243px; height: 145px; }
  .card-front .wordmark { left: 17px; top: 21px; font-size: 11px; }
  .card-front .wordmark .mark-square { width: 13px; height: 13px; }
  .card-holder { position: absolute; right: 17px; top: 21px; text-align: right; }
  .card-holder .holder-name { font-size: 7px; font-weight: 600; color: var(--navy); letter-spacing: 0.02em; }
  .card-holder .holder-name .surname { color: var(--orange); }
  .card-holder .holder-role { font-size: 6px; color: var(--muted); margin-top: 1px; }
  .card-holder .holder-rule { width: 21px; height: 0.6px; background: var(--muted); margin: 3px 0 0 auto; }
  .card-contacts { position: absolute; left: 17px; top: 82px; font-size: 4.6px; color: #555; line-height: 1.35; }
  .card-contacts .contact-row { margin-bottom: 3.6px; align-items: flex-start; }
  .card-contacts .icon { width: 6px; height: 6px; }

  /* Business card back */
  .card-back { left: 325px; top: 62px; width: 242px; height: 145px; background: var(--navy); }
  .card-back .wordmark { left: 51px; top: 63px; font-size: 17px; color: #fff; }
  .card-back .wordmark .mark-square { width: 18px; height: 18px; background: #fff; }

  /* Envelope back */
  .envelope-rear { position: absolute; left: 79px; top: 256px; width: 200px; height: 495px; }

  /* Envelope front */
  .envelope-front { left: 231px; top: 279px; width: 320px; height: 522px; background: transparent; }
  .envelope-front .envelope-body { position: absolute; left: 0; top: 70px; width: 320px; height: 452px; background: var(--paper); overflow: hidden; }
  .envelope-flap { position: absolute; left: 0; top: 0; width: 320px; height: 71px; }
  .flap-name { position: absolute; left: 0; top: 26px; width: 320px; text-align: center; color: #fff; font-weight: 600; font-size: 14px; letter-spacing: 0.04em; }
  .envelope-front .wordmark { left: 22px; top: 16px; font-size: 13px; }
  .envelope-front .wordmark .mark-square { width: 16px; height: 16px; }
  .address-window { position: absolute; left: 22px; top: 355px; width: 127px; height: 50px; border-radius: 4px; background: linear-gradient(160deg, #e3e4e7, var(--window)); border: 1px solid #c6c8cc; }
  .envelope-return { position: absolute; left: 22px; top: 418px; font-size: 5.2px; color: #555; }
  .envelope-return .icon { width: 6px; height: 6px; }

  /* Letterhead */
  .letterhead { left: 587px; top: 62px; width: 539px; height: 761px; }
  .letterhead .wordmark { left: 42px; top: 54px; font-size: 22px; }
  .letterhead .wordmark .mark-square { width: 26px; height: 26px; }
  .sender-contacts { position: absolute; right: 41px; top: 46px; font-size: 8px; color: #555; text-align: right; line-height: 1.25; }
  .sender-contacts .contact-row { justify-content: flex-end; gap: 5px; margin-bottom: 5px; }
  .sender-contacts .contact-row.address { align-items: flex-start; margin-bottom: 11px; }
  .sender-contacts .icon { width: 10px; height: 10px; }

  .recipient { position: absolute; left: 42px; top: 215px; }
  .recipient-name { font-size: 13px; font-weight: 600; color: var(--navy); letter-spacing: 0.03em; margin-bottom: 8px; }
  .recipient-line { font-size: 9.5px; color: var(--muted); line-height: 1.3; margin-bottom: 4px; }
  .letter-date { position: absolute; right: 40px; top: 295px; font-size: 11px; color: var(--muted); }
  .letter-body { position: absolute; left: 42px; top: 325px; width: 458px; font-size: 10px; font-weight: 300; color: var(--muted); line-height: 16.4px; text-align: justify; }
  .letter-body p + p { margin-top: 16px; }
  .sign-off { position: absolute; left: 42px; top: 555px; font-size: 15px; font-weight: 500; color: var(--ink); }
  .signature-area { position: absolute; left: 42px; top: 584px; width: 93px; height: 32px; background: linear-gradient(90deg, #eceef1, #f7f8f9); border-radius: 3px; }

  .corner-accent { position: absolute; left: 0; bottom: 0; display: block; }
</style>
</head>
<body>

  <svg width="0" height="0" style="position:absolute">
    <defs>
      <symbol id="icon-pin" viewBox="0 0 10 10"><rect width="10" height="10" fill="#0b0a6b"/><path d="M5 2a2.2 2.2 0 0 0-2.2 2.2C2.8 5.9 5 8.2 5 8.2s2.2-2.3 2.2-4A2.2 2.2 0 0 0 5 2z" fill="#fff"/><circle cx="5" cy="4.2" r="0.8" fill="#0b0a6b"/></symbol>
      <symbol id="icon-phone" viewBox="0 0 10 10"><rect width="10" height="10" fill="#ff6a13"/><path d="M3.2 2.2l1.1 1.3-.6.8c.4.8 1 1.4 1.9 1.9l.8-.6 1.3 1.1-.7 1c-2.3-.3-4.3-2.3-4.7-4.7z" fill="#fff"/></symbol>
      <symbol id="icon-mail" viewBox="0 0 10 10"><rect width="10" height="10" fill="#ff6a13"/><rect x="2" y="3" width="6" height="4.2" fill="none" stroke="#fff" stroke-width="0.8"/><path d="M2 3l3 2.4L8 3" fill="none" stroke="#fff" stroke-width="0.8"/></symbol>
      <symbol id="icon-web" viewBox="0 0 10 10"><rect width="10" height="10" fill="#ff6a13"/><path d="M3 2.2l4.2 2.9-1.8.4 1.1 2.1-.8.4-1.1-2.1-1.3 1.3z" fill="#fff"/></symbol>
    </defs>
  </svg>

  <!-- Business card: front -->
  <section class="sheet card-front" aria-label="Business card front">
    <div class="wordmark"><span class="mark-square"></span>VELTA HOME</div>
    <div class="card-holder">
      <div class="holder-name">MARCO L. <span class="surname">VENNER</span></div>
      <div class="holder-role">Managing Director</div>
      <div class="holder-rule"></div>
    </div>
    <div class="card-contacts">
      <div class="contact-row"><svg class="icon"><use href="#icon-pin"/></svg><span>Via dei Tigli 8<br>I-39100 Collina (Bz)</span></div>
      <div class="contact-row"><svg class="icon"><use href="#icon-phone"/></svg><span>+39 320 5550142</span></div>
      <div class="contact-row"><svg class="icon"><use href="#icon-mail"/></svg><span>office@veltahome.srl</span></div>
      <div class="contact-row"><svg class="icon"><use href="#icon-web"/></svg><span>www.veltahome.srl</span></div>
    </div>
    <svg class="corner-accent" width="243" height="145" viewBox="0 0 243 145">
      <polygon points="0,139 158,139 162,145 0,145" fill="var(--orange)"/>
      <polygon points="185,139 243,139 243,145 181,145" fill="var(--navy)"/>
    </svg>
  </section>

  <!-- Business card: back -->
  <section class="sheet card-back" aria-label="Business card back">
    <div class="wordmark"><span class="mark-square"></span>VELTA HOME</div>
    <svg class="corner-accent" width="242" height="145" viewBox="0 0 242 145">
      <polygon points="0,139 180,139 184,145 0,145" fill="var(--orange)"/>
      <path d="M191 145 Q212 98 242 65 L242 145 Z" fill="var(--green)"/>
    </svg>
  </section>

  <!-- Envelope: rear view -->
  <svg class="envelope-rear" viewBox="0 0 200 495" aria-label="Envelope back">
    <polygon points="0,66 28,0 200,0 200,495 0,495" fill="#fbfbfb"/>
    <path d="M0 66 L28 0 L200 0 L200 102 L40 102 Q25 102 15 90 Z" fill="#f3f4f5"/>
  </svg>

  <!-- Envelope: front -->
  <section class="sheet envelope-front" aria-label="Envelope front">
    <svg class="envelope-flap" viewBox="0 0 320 71">
      <path d="M0 71 L25 8 Q29 0 38 0 L282 0 Q291 0 295 8 L320 71 Z" fill="var(--navy)"/>
    </svg>
    <div class="flap-name">VELTA HOME</div>
    <div class="envelope-body">
      <div class="wordmark"><span class="mark-square"></span>VELTA HOME</div>
      <div class="address-window" aria-label="Recipient address window"></div>
      <div class="envelope-return contact-row"><svg class="icon"><use href="#icon-pin"/></svg><span>Via dei Tigli 8 &nbsp;I-39100 Collina (Bz)</span></div>
      <svg class="corner-accent" width="320" height="452" viewBox="0 0 320 452">
        <polygon points="0,435 235,435 238,440 0,440" fill="var(--navy)"/>
        <polygon points="0,444 241,444 246,452 0,452" fill="var(--orange)"/>
        <path d="M263 452 Q288 395 320 361 L320 452 Z" fill="var(--green)"/>
      </svg>
    </div>
  </section>

  <!-- Letterhead -->
  <section class="sheet letterhead" aria-label="A4 letterhead">
    <div class="wordmark"><span class="mark-square"></span>VELTA HOME</div>
    <div class="sender-contacts">
      <div class="contact-row address"><span>Via dei Tigli 8<br>I-39100 Collina (Bz)</span><svg class="icon"><use href="#icon-pin"/></svg></div>
      <div class="contact-row"><span>+39 320 5550142</span><svg class="icon"><use href="#icon-phone"/></svg></div>
      <div class="contact-row"><span>office@veltahome.srl</span><svg class="icon"><use href="#icon-mail"/></svg></div>
      <div class="contact-row"><span>www.veltahome.srl</span><svg class="icon"><use href="#icon-web"/></svg></div>
    </div>

    <div class="recipient">
      <div class="recipient-name">MR. ALAN REED</div>
      <div class="recipient-line">0100-555-014</div>
      <div class="recipient-line">alan.reed@mailbox.example</div>
      <div class="recipient-line">1234 City Your Ln. Suite<br>123 Dallas, TX 0000</div>
    </div>
    <div class="letter-date">12 December, 2025</div>

    <div class="letter-body">
      <p>Lorem ipsum dolor sit amet, consectetuer adipiscing elit, sed diam nonummy nibh euismod tincidunt ut laoreet dolore magna aliquam erat volutpat. Ut wisi enim ad minim veniam, quis nostrud exerci tation ullamcorper suscipit lobortis nisl ut aliquip ex ea commodo consequat. Duis autem vel eum iriure dolor in hendrerit in vulputate velit esse molestie consequat, vel illum dolore eu feugiat nulla facilisis at vero eros et accumsan et iusto odio dignissim qui blandit praesent luptatum zzril delenit augue duis dolore te feugait nulla facilisi.</p>
      <p>Lorem ipsum dolor sit amet, cons ectetuer adipiscing elit, sed diam nonummy nibh euismod tincidunt ut laoreet dolore magna aliquam erat volutpat. Ut wisi enim ad minim veniam, quis nostrud exerci tation ullamcorper suscipit lobortis nisl ut aliquip ex ea commodo consequat.</p>
    </div>

    <div class="sign-off">Mr. Alan Reed</div>
    <div class="signature-area" role="img" aria-label="Handwritten signature of the sender"></div>

    <svg class="corner-accent" width="539" height="761" viewBox="0 0 539 761">
      <polygon points="0,740 430,740 433,745 0,745" fill="var(--navy)"/>
      <polygon points="0,751 438,751 444,761 0,761" fill="var(--orange)"/>
      <path d="M466 761 Q497 695 539 647 L539 761 Z" fill="var(--green)"/>
    </svg>
  </section>

</body>
</html>
```